Business Card

To design a professional business card for myself a Beauty Therapist. I will be selling Sol Varenne tanning and other products from home (a beauty room). I have uploaded a file of there promo and I really love their colours. I'm looking for a classey feel to the design, simple but effective. I require my name Tessa Marlowe Beauty Therapist, Mobile- 0413952817, Email - tessa.marlowe@qelmail.com, Facebook - /tessamarlowebeauty & instagram - tessamarlowebeautytherapist . I would like the logo for facebook and instagram. I will also need a A5 & A4 flyer. text futura book to be used.

```html
<!DOCTYPE html>
<html lang="en">
<head>
<meta charset="utf-8">
<title>Tessa Marlowe – Beauty Therapist</title>
<link rel="stylesheet" href="https://fonts.googleapis.com/css2?family=Jost:wght@300;400&display=swap">
<style>
  :root {
    --paper: #ffffff;
    --ocean-deep: #0b5fb8;
    --ocean-mid: #1e86dc;
    --ocean-light: #3aa6ee;
    --sky-ink: #4cb0e8;
    --name-ink: #ffffff;
  }
  html, body {
    margin: 0;
    padding: 0;
    overflow: hidden;
    background: var(--paper);
  }
  .card {
    position: relative;
    width: 1200px;
    height: 702px;
    background: var(--paper);
    overflow: hidden;
    font-family: "Jost", "Futura", sans-serif;
  }
  .card__sea {
    position: absolute;
    inset: 0;
    clip-path: polygon(0 0, 974px 0, 486px 702px, 0 702px);
    background:
      radial-gradient(ellipse at 30% 20%, var(--ocean-light) 0%, transparent 60%),
      linear-gradient(170deg, var(--ocean-mid) 0%, var(--ocean-deep) 55%, var(--ocean-mid) 100%);
  }
  .identity {
    position: absolute;
    left: 72px;
    top: 296px;
    color: var(--name-ink);
    font-weight: 300;
    text-transform: uppercase;
    line-height: 1;
  }
  .identity__name {
    margin: 0;
    font-size: 70px;
    font-weight: 300;
    letter-spacing: 0.01em;
  }
  .identity__role {
    margin: 2px 0 0 12px;
    font-size: 44px;
    font-weight: 300;
    letter-spacing: 0.24em;
  }
  .contact {
    position: absolute;
    right: 48px;
    top: 512px;
    margin: 0;
    padding: 0;
    list-style: none;
    color: var(--sky-ink);
    font-size: 27px;
    font-weight: 400;
    line-height: 33.5px;
    text-align: right;
  }
  .contact__item {
    display: flex;
    justify-content: flex-end;
    align-items: center;
    white-space: nowrap;
  }
  .contact__email {
    text-transform: uppercase;
  }
  .contact__marker {
    display: inline-block;
    width: 24px;
    height: 24px;
    margin-right: 4px;
    background: var(--sky-ink);
  }
</style>
</head>
<body>
  <main class="card">
    <div class="card__sea" role="img" aria-label="Photograph of rippling blue ocean water"></div>

    <header class="identity">
      <h1 class="identity__name">Tessa Marlowe</h1>
      <p class="identity__role">Beauty Therapist</p>
    </header>

    <ul class="contact">
      <li class="contact__item">M: 0413952817</li>
      <li class="contact__item contact__email">E: tessa.marlowe@qelmail.com</li>
      <li class="contact__item"><span class="contact__marker" aria-hidden="true"></span>: tessamarlowebeauty</li>
      <li class="contact__item"><span class="contact__marker" aria-hidden="true"></span>: @tessamarlowebeautytherapist</li>
    </ul>
  </main>
</body>
</html>
```